Shine4all

Full service cleaning company. Specializing in commercial and apartment cleans.
Fully licensed and insured
Digital photos and invoices provided
for every job
For web designer...basic info as expected by a highend cleaning company that provides excellent service at reasonable pricing. We are going after large property management companies as well as not pricing ourselves out to help the local mom and pop companies as well.
Updates

Project Deadline Extended Reason: Everyone seems to be having trouble understanding that we are a dumpster company that is adding a cleaning side to the company. We want our clients to see Shine4All as a separate branch of our our already established waste management company.We are not a regular cleaning company. We specialize in going after large commercial cleans and apartment cleans. I have now included info regarding a proposal for work and our invoice/job completion to make it clearer what we do Added Monday, July 20, 2015

Target Market(s)

Property Management companies in Savannah, Richmond Hill, Rincon, Hinesville and Midway Georgia

Industry/Entity Type

Cleaning Service

Coding

Coded - Design and coding required

Number of Pages Required

3 page

Requirements
Must have
• Nice home page with lots of photos (stock are fine) to convey exactly what we do (getting logo bid on right now on this sight).
• Information page with employee photos (can leave blank) need room for 4 photos and bios.
• Page or link to a static page for the dumpster company BinTrek (logo for this is red and black file attached along with photo of dumpster. This page just needs to be one page with contact info and information about commercial dumpster.
• Basically this site is just a fluff page used for marketing purposes. Its content can be general and once created wont change much. Services and photos can be provided upon request but general layout and info is what we are looking for.

```html
<!DOCTYPE html>
<html lang="en">
<head>
<meta charset="utf-8">
<title>Shine4All – Commercial Cleaning</title>
<link href="https://fonts.googleapis.com/css2?family=Roboto:wght@400;700&family=Roboto+Condensed:wght@400;700&display=swap" rel="stylesheet">
<style>
:root{
  --red:#e0262a;
  --dark:#111;
  --footer:#232323;
  --grey-band:#ececec;
  --text:#555;
  --light:#999;
  --white:#fff;
}
*{box-sizing:border-box;margin:0;padding:0}
html,body{width:726px;height:1200px;overflow:hidden;background:var(--white)}
body{font-family:"Roboto",Arial,sans-serif;font-size:7px;color:var(--text);line-height:1.55}
h2,h3,.nav a,.btn,.hero-title,.brand{font-family:"Roboto Condensed",Arial Narrow,sans-serif}
.wrap{width:650px;margin:0 auto;position:relative}
.brand{color:var(--red);font-weight:700;display:flex;align-items:center;gap:6px;letter-spacing:1px}
.brand .mark{width:9px;height:9px;background:var(--red)}
.btn{display:inline-block;background:#333;color:var(--white);font-size:7px;padding:6px 11px;font-weight:700;text-transform:uppercase}
.btn.red{background:var(--red)}
.photo{background:linear-gradient(135deg,#9aa0a8,#c9ccd1)}

/* header */
.header{height:74px}
.header .wrap{height:74px}
.header .brand{position:absolute;left:0;top:12px;font-size:28px}
.topline{position:absolute;right:0;top:12px;display:flex;gap:16px;font-size:7px;color:#444}
.topline span{display:flex;align-items:center;gap:4px}
.nav{position:absolute;right:0;top:44px;display:flex;gap:4px}
.nav a{font-size:7.5px;color:#333;text-decoration:none;padding:5px 10px;font-weight:700}
.nav a.active{background:var(--red);color:var(--white)}

/* hero */
.hero{height:286px;position:relative;background:linear-gradient(90deg,#d9dadc 0%,#b9bcc0 45%,#8d949c 100%)}
.hero-copy{position:absolute;left:38px;top:88px;width:260px}
.hero-title{color:var(--red);font-size:29px;font-weight:700;line-height:1}
.hero-copy p{font-size:12px;color:#333;margin:8px 0 14px;line-height:1.25}
.dots{position:absolute;left:38px;top:254px;display:flex;gap:5px}
.dots i{width:8px;height:8px;border-radius:50%;background:#333}
.dots i:first-child{background:var(--red)}

/* welcome */
.welcome{height:136px}
.welcome .wrap{display:flex;height:136px;align-items:center}
.welcome .brand{width:290px;font-size:48px;justify-content:center}
.welcome .brand .mark{width:20px;height:20px}
.welcome-copy{flex:1;padding-left:20px}
h2{color:var(--red);font-size:14px;font-weight:700;text-transform:uppercase;margin-bottom:6px}

/* services */
.services{background:var(--dark);height:165px;color:#bbb}
.services .wrap{display:flex;padding-top:18px;gap:22px}
.services-copy{width:290px}
.services-copy p{margin-bottom:12px}
.service-cards{display:flex;gap:12px}
.card{width:150px}
.card .photo{height:98px}
.card .label{background:var(--red);color:var(--white);text-align:center;font-family:"Roboto Condensed",sans-serif;font-weight:700;font-size:10px;padding:5px 0}

/* why & testimonials */
.why{height:170px}
.why .wrap{display:flex;padding-top:22px;gap:40px}
.why-col{width:300px}
.why-row{display:flex;gap:10px}
.why-row .photo{width:95px;height:68px;flex:none}
.why-row .text p{margin-bottom:8px}
.quote{background:#f2f2f2;padding:10px 12px;position:relative;display:flex;gap:6px}
.quote svg{flex:none}
.quote:after{content:"";position:absolute;left:18px;bottom:-7px;border:7px solid transparent;border-top-color:#f2f2f2;border-bottom:0}
.quote-name{color:var(--red);margin-top:12px;margin-left:12px}

/* jobs & bio */
.jobs{background:var(--grey-band);height:195px}
.jobs .wrap{display:flex;padding-top:20px;gap:30px}
.jobs-col{width:400px}
.job-list{display:flex;gap:12px}
.job{width:120px}
.job .photo{height:68px;margin-bottom:6px}
.job .cap{color:var(--red);line-height:1.3}
.bio{flex:1}
.bio-row{display:flex;gap:10px}
.bio-row .photo{width:58px;height:64px;flex:none}
.bio-name{color:var(--red);font-weight:700;font-size:8px}
.arrows{display:flex;gap:4px;margin-top:10px}
.arrows i{width:11px;height:11px;border-radius:50%;border:1px solid #888}

/* footer */
.footer{background:var(--footer);height:180px;color:#aaa}
.footer .wrap{display:flex;padding-top:18px;gap:40px}
.footer h2{font-size:14px}
.contact{width:170px}
.contact strong{color:var(--white);display:block}
.socials{display:flex;gap:3px;margin-top:8px}
.socials i{width:10px;height:10px;background:#555}
.map{width:440px;height:92px;background:linear-gradient(135deg,#cfd6c4,#e6e3d6 60%,#bcc9d3)}
.copyright{position:absolute;right:38px;bottom:8px;font-size:6px;color:#888}
</style>
</head>
<body>

<header class="header">
  <div class="wrap">
    <div class="brand"><span class="mark"></span>BinTrek</div>
    <div class="topline">
      <span><svg width="8" height="8" viewBox="0 0 10 10"><path d="M2 1l2 2-1 1.5c.6 1.2 1.3 1.9 2.5 2.5L7 6l2 2-1.5 1.5C4 9 1 6 .5 2.5z" fill="var(--red)"/></svg>Call: 912-555-0147</span>
      <span><svg width="9" height="7" viewBox="0 0 10 8"><rect x=".5" y=".5" width="9" height="7" fill="none" stroke="var(--red)"/><path d="M.5 .5l4.5 4 4.5-4" fill="none" stroke="var(--red)"/></svg>Email: hello@shine4all-clean.com</span>
    </div>
    <nav class="nav">
      <a class="active">HOME</a><a>BIO</a><a>BINTREK</a><a>CONTACT US</a>
    </nav>
  </div>
</header>

<section class="hero photo" role="img" aria-label="Cleaner operating a floor scrubbing machine in a bright office corridor">
  <div class="hero-copy">
    <div class="hero-title">COMMERCIAL CLEANING</div>
    <p>Aenean lacinia sodales eros, sit amet molestie ante consectetur eget. Sed vel magna vel eros adipiscing adipiscing eu et amet turpis.</p>
    <span class="btn">Contact us</span>
  </div>
  <div class="dots"><i></i><i></i><i></i></div>
</section>

<section class="welcome">
  <div class="wrap">
    <div class="brand"><span class="mark"></span>BinTrek</div>
    <div class="welcome-copy">
      <h2>Welcome to our website</h2>
      <p>Vestibulum et metus sit amet justo bibendum tincidunt sit amet quam. Pellentesque fermentum tincidunt lorem at lacus sit malesuada finibus. Nunc consequat congue lectus imperdiet. Donec in nisi vitae, sit malesuada justo. Nunc at sit a justo vehicula tempor. Fusce dignissim luctus vestibulum placerat lacinia. Aenean lacinia sodales eros, sit amet molestie ante consectetur eget. Sed vel magna vel eros adipiscing adipiscing eu et amet.</p>
    </div>
  </div>
</section>

<section class="services">
  <div class="wrap">
    <div class="services-copy">
      <h2>Our services offer</h2>
      <p>Vestibulum et metus sit amet justo bibendum tincidunt sit amet quam. Pellentesque fermentum lorem at lacus finibus malesuada. Nunc consequat congue lectus imperdiet. Donec in nisi vitae, sit malesuada justo. Nunc at justo vehicula tempor. Fusce dignissim luctus vestibulum placerat.</p>
      <span class="btn">Read more</span>
    </div>
    <div class="service-cards">
      <div class="card"><div class="photo" role="img" aria-label="Worker cleaning a commercial office floor"></div><div class="label">COMMERCIAL</div></div>
      <div class="card"><div class="photo" role="img" aria-label="Cleaner tidying an apartment interior"></div><div class="label">APARTMENT</div></div>
    </div>
  </div>
</section>

<section class="why">
  <div class="wrap">
    <div class="why-col">
      <h2>Why BinTrek</h2>
      <div class="why-row">
        <div class="photo" role="img" aria-label="Red and black roll-off dumpster on a truck"></div>
        <div class="text">
          <p>Vestibulum et metus sit amet justo bibendum tincidunt sit amet quam. Pellentesque fermentum lorem at lacus finibus malesuada. Nunc consequat congue lectus imperdiet. Donec in nisi vitae, sit malesuada justo. Nunc at justo vehicula tempor dignissim luctus.</p>
          <span class="btn">Read more</span>
        </div>
      </div>
    </div>
    <div class="why-col">
      <h2>Testimonials</h2>
      <div class="quote">
        <svg width="10" height="8" viewBox="0 0 10 8"><path d="M0 8V4l2-4h2L3 4h1v4zm6 0V4l2-4h2L9 4h1v4z" fill="#bbb"/></svg>
        <p>Nunc a leo et turpis blandit varius dapibus quis dui. Pellentesque tortor vitae sed pulvinar tincidunt lorem. Integer aliquet tortor vitae pulvinar tincidunt, blandit arcu nisl ac justo.</p>
      </div>
      <div class="quote-name">Name Heading</div>
    </div>
  </div>
</section>

<section class="jobs">
  <div class="wrap">
    <div class="jobs-col">
      <h2>Recent jobs</h2>
      <div class="job-list">
        <div class="job"><div class="photo" role="img" aria-label="Cleaned office lobby"></div><div class="cap">Vestibulum vel metus<br>sit amet turpis</div></div>
        <div class="job"><div class="photo" role="img" aria-label="Crew cleaning an apartment kitchen"></div><div class="cap">Vestibulum vel metus<br>sit amet turpis</div></div>
        <div class="job"><div class="photo" role="img" aria-label="Cleaner polishing a commercial floor"></div><div class="cap">Vestibulum vel metus<br>sit amet turpis</div></div>
      </div>
    </div>
    <div class="bio">
      <h2>Bio</h2>
      <div class="bio-row">
        <div class="photo" role="img" aria-label="Staff portrait placeholder"></div>
        <div>
          <div class="bio-name">Name Heading</div>
          <p>Vestibulum et metus sit amet justo bibendum tincidunt. Pellentesque fermentum lorem at lacus malesuada finibus congue.</p>
          <span style="color:var(--red)">Read more</span>
        </div>
      </div>
      <div class="arrows"><i></i><i></i></div>
    </div>
  </div>
</section>

<footer class="footer">
  <div class="wrap">
    <div class="contact">
      <h2>Contact us</h2>
      <strong>SHINE4ALL CLEANING</strong>
      <p>4120 Harbor Bend Rd<br>Savannah, GA 31401<br>Ph: 912-555-0147<br>Email: hello@shine4all-clean.com</p>
      <div class="socials"><i></i><i></i><i></i><i></i></div>
    </div>
    <div>
      <h2>Our location</h2>
      <div class="map" role="img" aria-label="Street map of the service area"></div>
    </div>
  </div>
  <div class="copyright">Copyright © 2015, Shine4All Cleaning. All Right Reserved</div>
</footer>

</body>
</html>
```